Business Cards and Stationary Design for Landscaping Company
Merriweather's Yard Crafting
Business Cards and Stationary Design for Landscaping Company - Home and Garden
Creative Brief
Simple
Dennis Carraway
President
PO Box 48213 Houston, TX 77241-4821
myc@merriweatheryard.com
www.merriweatheryard.com
Please make the YARD CRAFTING the same color as the light color swish

```html
<!DOCTYPE html>
<html lang="en">
<head>
<meta charset="utf-8">
<title>Merriweather's Yard Crafting — Business Card</title>
<link rel="stylesheet" href="https://fonts.googleapis.com/css2?family=Cinzel:wght@700&family=Open+Sans:wght@400;600&display=swap">
<style>
  :root {
    --forest: #1f4a2b;
    --leaf: #7ab648;
    --paper: #ffffff;
    --ink: #2c2c2c;
    --rule: #b9bdb8;
    --backdrop: #e4e5e2;
  }
  html, body {
    margin: 0;
    padding: 0;
    width: 1200px;
    height: 782px;
    overflow: hidden;
    background: var(--backdrop);
  }
  .sheet {
    position: relative;
    width: 1200px;
    height: 782px;
    display: flex;
    flex-direction: column;
    align-items: center;
    justify-content: center;
    gap: 30px;
  }
  .card {
    position: relative;
    width: 620px;
    height: 354px;
    background: var(--paper);
    border-radius: 22px;
    overflow: hidden;
    box-shadow: 0 2px 8px rgba(0,0,0,0.12);
  }
  .card__swoosh {
    position: absolute;
    inset: 0;
    width: 100%;
    height: 100%;
  }
  .swoosh-band { fill: var(--forest); }
  .swoosh-accent { fill: var(--leaf); }

  .brand {
    position: absolute;
    display: flex;
    flex-direction: column;
    align-items: center;
    font-family: 'Cinzel', serif;
  }
  .brand__dot {
    width: 58px;
    height: 58px;
    border-radius: 50%;
    background: var(--forest);
    margin-bottom: 10px;
  }
  .brand__name {
    font-weight: 700;
    font-size: 30px;
    color: var(--forest);
    letter-spacing: 0.5px;
    line-height: 1;
  }
  .brand__tagline {
    font-weight: 700;
    font-size: 10px;
    color: var(--leaf);
    letter-spacing: 2.5px;
    margin-top: 5px;
  }
  .card--back .brand { left: 0; right: 0; top: 120px; }
  .card--front .brand { left: 40px; top: 118px; }
  .card--front .brand__name { font-size: 28px; }

  .holder {
    position: absolute;
    right: 26px;
    top: 86px;
    text-align: right;
    font-family: 'Open Sans', sans-serif;
    color: var(--paper);
  }
  .holder__name { font-size: 17px; font-weight: 600; line-height: 1.2; }
  .holder__title { font-size: 14px; line-height: 1.3; }

  .contact {
    position: absolute;
    left: 355px;
    top: 178px;
    padding-left: 14px;
    border-left: 1px solid var(--rule);
    font-family: 'Open Sans', sans-serif;
    font-size: 13px;
    line-height: 1.55;
    color: var(--ink);
  }
  .contact__row { display: flex; align-items: center; gap: 6px; }
  .contact__icon { width: 11px; height: 11px; fill: var(--ink); flex: none; }
</style>
</head>
<body>
<main class="sheet">

  <section class="card card--back" aria-label="Card back">
    <svg class="card__swoosh" viewBox="0 0 620 354" preserveAspectRatio="none" aria-hidden="true">
      <path class="swoosh-band" d="M60,0 H620 V92 C470,40 280,22 60,0 Z"/>
      <path class="swoosh-accent" d="M0,22 C230,22 470,50 620,108 V120 C470,66 240,36 0,30 Z"/>
    </svg>
    <div class="brand">
      <div class="brand__dot"></div>
      <div class="brand__name">MERRIWEATHER'S</div>
      <div class="brand__tagline">YARD CRAFTING</div>
    </div>
  </section>

  <section class="card card--front" aria-label="Card front">
    <svg class="card__swoosh" viewBox="0 0 620 354" preserveAspectRatio="none" aria-hidden="true">
      <path class="swoosh-band" d="M0,0 H620 V168 C470,95 270,55 0,44 Z"/>
      <path class="swoosh-accent" d="M0,54 C260,62 470,110 620,184 V196 C470,124 260,76 0,62 Z"/>
    </svg>
    <div class="brand">
      <div class="brand__dot"></div>
      <div class="brand__name">MERRIWEATHER'S</div>
      <div class="brand__tagline">YARD CRAFTING</div>
    </div>
    <div class="holder">
      <div class="holder__name">Dennis Carraway</div>
      <div class="holder__title">President</div>
    </div>
    <div class="contact">
      <div>PO Box 48213</div>
      <div>Houston, TX 77241-4821</div>
      <div class="contact__row">
        <svg class="contact__icon" viewBox="0 0 12 12" aria-hidden="true"><path d="M2.5,0.5 L4.5,0.5 L5.3,3 L4,4 C4.6,5.6 6.4,7.4 8,8 L9,6.7 L11.5,7.5 L11.5,9.5 C11.5,10.6 10.6,11.5 9.5,11.5 C4.5,11.3 0.7,7.5 0.5,2.5 C0.5,1.4 1.4,0.5 2.5,0.5 Z"/></svg>
        <span>713 555 0142</span>
      </div>
      <div class="contact__row">
        <svg class="contact__icon" viewBox="0 0 12 12" aria-hidden="true"><path d="M3,0 H9 A1,1 0 0 1 10,1 V11 A1,1 0 0 1 9,12 H3 A1,1 0 0 1 2,11 V1 A1,1 0 0 1 3,0 Z M3.2,1.5 V9 H8.8 V1.5 Z"/></svg>
        <span>713 555 0187</span>
      </div>
      <div class="contact__row">
        <svg class="contact__icon" viewBox="0 0 12 12" aria-hidden="true"><path d="M0.5,2 H11.5 V10 H0.5 Z M1.5,3 V3.4 L6,6.6 L10.5,3.4 V3 Z"/></svg>
        <span>myc@merriweatheryard.com</span>
      </div>
      <div>www.merriweatheryard.com</div>
    </div>
  </section>

</main>
</body>
</html>
```